Support People to improve their image and well-being by provided personalised advise

We need a design for business cards that could be used for production on plato press. We build a new business in our region for advising mostly women (also men though) on style embracing several aspects including fashion, style, self-confidence and ultimately your internal and external image. The business card should be "classy", "french-style". The business is located in the french -speaking part of Switzerland, close to France. The name of the company is Velo Grace

Target Market(s)

Service fees won't be cheap (medium to premium) thus we target mid-class to upper-class women (1st target) and men (2nd target)

Industry/Entity Type

Life Coaching

Contact Information for Business Card

Conseil en Image

+41 79 418 62 07
morinetu@velo-grace.ch
linkedin.com/in/tu-moro-netia

Logo Text

Velo Grace

Colors

Designer to choose colors to be used in the design.

```html
<!DOCTYPE html>
<html lang="fr">
<head>
<meta charset="utf-8">
<title>Velo Grace – Cartes de visite</title>
<link href="https://fonts.googleapis.com/css2?family=Jost:wght@400;500&family=Kaushan+Script&display=swap" rel="stylesheet">
<style>
  :root {
    --backdrop: #b9b9b9;
    --charcoal: #373b3e;
    --paper: #f4f4f3;
    --gold: #c9a66f;
    --gold-light: #e8cf9e;
    --gold-deep: #b48f5c;
    --silver: #c8c9c9;
    --ink: #2f3235;
  }
  * { box-sizing: border-box; margin: 0; padding: 0; }
  html, body { width: 1200px; height: 576px; overflow: hidden; }
  body {
    background: var(--backdrop);
    font-family: "Jost", "Futura", sans-serif;
    position: relative;
  }
  .card {
    position: absolute;
    top: 138px;
    width: 484px;
    height: 294px;
    border-radius: 14px;
    overflow: hidden;
  }
  .card--back { left: 82px; background: var(--charcoal); }
  .card--front { left: 602px; width: 482px; background: var(--paper); }

  .brand-mark {
    position: absolute;
    border-radius: 50%;
    background: var(--gold);
  }
  .card--back .brand-mark { width: 62px; height: 62px; left: 211px; top: 96px; }
  .card--front .brand-mark { width: 54px; height: 54px; left: 102px; top: 68px; }

  .brand-name {
    position: absolute;
    font-weight: 400;
    letter-spacing: 0.2em;
    white-space: nowrap;
    text-transform: uppercase;
    font-size: 25px;
  }
  .card--back .brand-name {
    left: 0; right: 0; top: 181px;
    text-align: center;
    color: var(--silver);
  }
  .card--front .brand-name {
    left: 38px; top: 150px;
    color: var(--ink);
  }

  .accent-band {
    position: absolute;
    left: 0;
    right: 0;
    bottom: 0;
    height: 102px;
    background: linear-gradient(100deg, var(--gold-deep) 0%, var(--gold) 45%, var(--gold-light) 100%);
  }

  .person {
    position: absolute;
    right: 32px;
    top: 44px;
    text-align: right;
  }
  .person__name {
    font-family: "Kaushan Script", cursive;
    font-size: 24px;
    color: var(--gold-deep);
    line-height: 1.2;
  }
  .person__role {
    font-size: 12.5px;
    color: var(--ink);
    margin-top: 4px;
  }

  .contact {
    position: absolute;
    right: 32px;
    top: 208px;
    list-style: none;
    text-align: right;
  }
  .contact__item {
    display: flex;
    justify-content: flex-end;
    align-items: center;
    gap: 8px;
    font-size: 12.5px;
    color: var(--ink);
    height: 18.5px;
    white-space: nowrap;
  }
  .contact__icon { width: 11px; height: 11px; fill: var(--ink); }
  .contact__icon--line { fill: none; stroke: var(--ink); }
</style>
</head>
<body>
  <section class="card card--back" aria-label="Verso de la carte">
    <span class="brand-mark"></span>
    <p class="brand-name">Velo Grace</p>
  </section>

  <section class="card card--front" aria-label="Recto de la carte">
    <div class="accent-band" role="img" aria-label="Bande décorative ondulée or et anthracite"></div>

    <span class="brand-mark"></span>
    <p class="brand-name">Velo Grace</p>

    <div class="person">
      <p class="person__name">Tu Moro Netia</p>
      <p class="person__role">Conseil en Image</p>
    </div>

    <ul class="contact">
      <li class="contact__item">+41 79 418 62 07
        <svg class="contact__icon" viewBox="0 0 12 12" aria-hidden="true"><path d="M1,4 C1,2 3,1.5 6,1.5 C9,1.5 11,2 11,4 L8.5,4.5 L8.5,3.5 L3.5,3.5 L3.5,4.5 Z M2.5,10.5 L3.5,5.5 L8.5,5.5 L9.5,10.5 Z"/></svg>
      </li>
      <li class="contact__item">morinetu@velo-grace.ch
        <svg class="contact__icon" viewBox="0 0 12 12" aria-hidden="true"><path d="M1,2.5 H11 V9.5 H1 Z M1.8,3.2 L6,6.4 L10.2,3.2 Z" fill-rule="evenodd"/></svg>
      </li>
      <li class="contact__item">www.velo-grace.ch
        <svg class="contact__icon contact__icon--line" viewBox="0 0 12 12" aria-hidden="true"><circle cx="6" cy="6" r="5" stroke-width="1.2"/><path d="M1,6 H11 M6,1 C3.5,3.5 3.5,8.5 6,11 M6,1 C8.5,3.5 8.5,8.5 6,11" stroke-width="1"/></svg>
      </li>
    </ul>
  </section>
</body>
</html>
```